Business Card Design Project

Hi,
I am after a business card design for a new business. The business is called Quarrel Works and is a stockist of building supplies used for modern cosmetic renovations for houses. (e.g Floorboards, timber decking, modern fittings and fixtures.)
The logo and font faces have been attached.
The logo comes in 2 different color scheme's - 1. Orange on White & 2. Orange on Black. I would like 2 versions of the business card design to reflect these color scheme's.
The designs need to be double sided. The front should contain all the contact information, whilst the back of the card should display the logo and the URL of the webpage - www.quarrelworks-demo.com.au . The logo needs to be displayed creatively on the back of the card.
The business card design needs to reflect the image of modern living, but should also have the wow factor.

```html
<!DOCTYPE html>
<html lang="en">
<head>
<meta charset="utf-8">
<title>Quarrel Works – Business Card Options</title>
<link rel="stylesheet" href="https://fonts.googleapis.com/css2?family=Work+Sans:wght@300;400&family=Open+Sans:ital,wght@0,400;1,400&display=swap">
<style>
  :root {
    --sheet: #ffffff;
    --ink: #111111;
    --brown-deep: #2e140d;
    --brown-night: #170907;
    --rust: #a84626;
    --orange: #f26a25;
    --white: #ffffff;
    --cream: #f3e9e3;
  }
  * { margin: 0; padding: 0; box-sizing: border-box; }
  html, body { width: 1200px; height: 900px; overflow: hidden; background: var(--sheet); }
  body { position: relative; font-family: "Open Sans", Verdana, sans-serif; color: var(--ink); }

  .option-label { position: absolute; left: 18px; font-size: 17px; }
  .side-label { position: absolute; width: 120px; margin-left: -60px; text-align: center; font-size: 17px; text-decoration: underline; }

  .card { position: absolute; overflow: hidden; }
  .card svg { position: absolute; left: 0; top: 0; }

  .contact { position: absolute; font-size: 8.5px; font-style: italic; color: var(--white); line-height: 13.5px; }
  .contact span { display: inline-block; width: 42px; }

  .wordmark { position: absolute; font-family: "Work Sans", Helvetica, sans-serif; font-weight: 300; line-height: 1; }
  .wordmark .line { display: block; }

  .trades { position: absolute; left: 0; right: 0; text-align: center; font-size: 7.5px; color: var(--white); }
  .web { position: absolute; font-size: 8.5px; font-style: italic; color: var(--white); }

  .mark-square { position: absolute; background: var(--orange); }
  .entity { position: absolute; font-family: "Work Sans", Helvetica, sans-serif; font-weight: 300; font-size: 22px; color: var(--cream); transform: rotate(-90deg); transform-origin: left top; white-space: nowrap; }
</style>
</head>
<body>

  <!-- Option 3 -->
  <div class="option-label" style="top:32px;">Option-3</div>

  <section class="card card-front" style="left:17px; top:62px; width:561px; height:301px; background:var(--rust);">
    <div style="position:absolute; left:0; top:0; width:100%; height:65px; background:var(--brown-deep); border-bottom:2px solid var(--orange);"></div>
    <div style="position:absolute; left:0; bottom:0; width:100%; height:18px; background:var(--brown-deep);"></div>
    <div class="contact" style="left:419px; top:7px;">
      <div><span>Phone</span>(+61) 000-55501-000</div>
      <div><span>Mobile</span>(+61) 000-55501-000</div>
      <div>hello@quarrelworks-demo.com.au</div>
    </div>
    <div class="wordmark" style="left:157px; top:110px; font-size:54px; color:var(--white);">
      <span class="line">Quarrel</span><span class="line" style="margin-top:8px;">Works</span>
    </div>
    <div class="trades" style="bottom:4px;">We deal in : Floorboards, timber decking, modern fittings and fixtures</div>
  </section>
  <div class="side-label" style="left:232px; top:370px;">Front</div>

  <section class="card card-back" style="left:618px; top:63px; width:562px; height:302px; background:var(--brown-deep);">
    <div class="mark-square" style="left:88px; top:101px; width:80px; height:80px;"></div>
    <div class="wordmark" style="left:200px; top:92px; font-size:46px; color:var(--orange);">
      <span class="line">Quarrel</span><span class="line" style="margin-top:6px;">Works</span>
    </div>
    <div class="entity" style="left:447px; top:182px;">pty ltd</div>
    <div class="web" style="left:10px; top:285px;">www.quarrelworks-demo.com.au</div>
  </section>
  <div class="side-label" style="left:890px; top:370px;">Back</div>

  <!-- Option 4 -->
  <div class="option-label" style="top:473px;">Option-4</div>

  <section class="card card-front" style="left:17px; top:502px; width:566px; height:306px; background:var(--rust);">
    <svg width="566" height="306" viewBox="0 0 566 306" aria-hidden="true">
      <polygon points="0,82 160,28 566,102 566,306 0,306" fill="var(--brown-night)"/>
      <polyline points="0,82 160,28 566,102" fill="none" stroke="var(--white)" stroke-width="1.6"/>
      <rect x="0" y="286" width="566" height="20" fill="#220d08"/>
    </svg>
    <div class="contact" style="left:424px; top:13px;">
      <div><span>Phone</span>(+61) 000-55501-000</div>
      <div><span>Mobile</span>(+61) 000-55501-000</div>
      <div>hello@quarrelworks-demo.com.au</div>
    </div>
    <div class="wordmark" style="left:140px; top:110px; font-size:54px; color:var(--white);">
      <span class="line">Quarrel</span><span class="line" style="margin-top:8px;">Works</span>
    </div>
    <div class="trades" style="bottom:5px;">We deal in : Floorboards, timber decking, modern fittings and fixtures</div>
  </section>
  <div class="side-label" style="left:232px; top:815px;">Front</div>

  <section class="card card-back" style="left:612px; top:495px; width:568px; height:305px; background:var(--brown-night);">
    <div class="mark-square" style="left:114px; top:112px; width:88px; height:88px;"></div>
    <div class="wordmark" style="left:236px; top:102px; font-size:46px; color:var(--orange);">
      <span class="line">Quarrel</span><span class="line" style="margin-top:6px;">Works</span>
    </div>
    <div class="entity" style="left:486px; top:192px;">pty ltd</div>
    <div class="web" style="right:10px; top:287px;">www.quarrelworks-demo.com.au</div>
  </section>
  <div class="side-label" style="left:890px; top:815px;">Back</div>

</body>
</html>
```